Design Card that Captures Life's Moments

Thinking black and white design with maybe some accent colors. Open to others too. Looking for bold and modern to accompany new logo design. For the side without my info, would have tagline of "Capturing Life's Moments" with either logo or website petravossimaging.com. I want the tagline to dominate and be the main focus of that side.

Target Market(s)

Something that can appeal to people who might be interested in family/kids, business, sports, commercial, or birth/newborn photography.

Industry/Entity Type

Professional Photography

Contact Information for Business Card

Font styles to use
Sans Serif
Script
Other font styles liked:
• Go with Logo, but the tagline could be script that popped.

Requirements
Must have
• See details above! Wow factor! Make someone pick my card up and take it home or at least to look at it further.
• Tagline: Capturing Life's Moments (Main text on side without name)
• INFO:
• Petra Voss-Hale - Photographer
• 555-318-0462 - Cell and for SMS
• www.petravossimaging.com - Website (maybe on side with tagline?)
• petra@petrastudioframes.com - Email
Nice to have
• JUST AN IDEA... I would like to see Capturing Life's Moment really take over most of one side of the card. Think greeting card. Where you can't miss it. It is in your face, but nice and elegant. Maybe cursive, but could work with other font. Instead of logo on tagline side, just have petravossimaging.com in smaller text along one of the edges.
Should not have
• Too simple I could of created it, like with only my logo and some typed text.

```html
<!DOCTYPE html>
<html lang="en">
<head>
<meta charset="utf-8">
<title>Petra Voss Photography – Business Card</title>
<link href="https://fonts.googleapis.com/css2?family=Questrial&display=swap" rel="stylesheet">
<style>
  :root {
    --backdrop: #efe9df;
    --card: #000000;
    --ink: #ffffff;
  }
  * { margin: 0; padding: 0; box-sizing: border-box; }
  html, body {
    width: 1189px;
    height: 1200px;
    overflow: hidden;
    background: var(--backdrop);
    font-family: "Questrial", sans-serif;
    color: var(--ink);
  }
  .card {
    position: absolute;
    left: 171px;
    width: 856px;
    height: 487px;
    background: var(--card);
    overflow: hidden;
  }
  .card--front { top: 68px; }
  .card--back { top: 627px; }

  .brand {
    position: absolute;
    right: 99px;
    text-align: right;
  }
  .brand__name {
    display: block;
    line-height: 1;
    letter-spacing: 1px;
  }
  .brand__sub {
    display: block;
    letter-spacing: 13px;
    margin-right: -13px;
  }

  .card--front .brand { top: 78px; }
  .card--front .brand__name { font-size: 100px; }
  .card--front .brand__sub { font-size: 22px; margin-top: 12px; }

  .person {
    position: absolute;
    right: 554px;
    top: 349px;
    text-align: right;
  }
  .person__name { font-size: 30px; line-height: 1.1; }
  .person__role { font-size: 23px; line-height: 1.2; }

  .divider {
    position: absolute;
    left: 333px;
    top: 340px;
    width: 2px;
    height: 90px;
    background: var(--ink);
  }

  .contacts {
    position: absolute;
    left: 362px;
    top: 339px;
    list-style: none;
  }
  .contacts__item {
    display: flex;
    align-items: center;
    height: 31px;
    font-size: 24px;
    white-space: nowrap;
  }
  .contacts__icon {
    width: 22px;
    height: 22px;
    margin-right: 13px;
    flex: none;
  }

  .card--back .brand { top: 62px; }
  .card--back .brand__name { font-size: 54px; }
  .card--back .brand__sub { font-size: 15px; margin-top: 8px; letter-spacing: 9px; margin-right: -9px; }

  .tagline {
    position: absolute;
    left: 60px;
    right: 99px;
    top: 220px;
    text-align: right;
    font-size: 58px;
    line-height: 1.15;
    white-space: nowrap;
  }
</style>
</head>
<body>

<section class="card card--front">
  <div class="brand">
    <span class="brand__name">Petra Voss</span>
    <span class="brand__sub">PHOTOGRAPHY</span>
  </div>

  <div class="person">
    <p class="person__name">Petra Voss-Hale</p>
    <p class="person__role">Photographer</p>
  </div>

  <div class="divider"></div>

  <ul class="contacts">
    <li class="contacts__item">
      <svg class="contacts__icon" viewBox="0 0 22 22" aria-hidden="true">
        <rect x="1" y="1" width="20" height="20" fill="#fff"/>
        <rect x="7" y="4" width="8" height="14" fill="none" stroke="#000" stroke-width="1.5"/>
        <rect x="8.5" y="11" width="5" height="5" fill="#000"/>
      </svg>
      555-318-0462 - Cell and for SMS
    </li>
    <li class="contacts__item">
      <svg class="contacts__icon" viewBox="0 0 22 22" aria-hidden="true">
        <circle cx="11" cy="11" r="10" fill="#fff"/>
        <g fill="none" stroke="#000" stroke-width="1">
          <circle cx="11" cy="11" r="7"/>
          <ellipse cx="11" cy="11" rx="3" ry="7"/>
          <line x1="4" y1="11" x2="18" y2="11"/>
          <line x1="11" y1="4" x2="11" y2="18"/>
          <line x1="5" y1="7.5" x2="17" y2="7.5"/>
          <line x1="5" y1="14.5" x2="17" y2="14.5"/>
        </g>
      </svg>
      www.petravossimaging.com
    </li>
    <li class="contacts__item">
      <svg class="contacts__icon" viewBox="0 0 22 22" aria-hidden="true">
        <rect x="1" y="1" width="20" height="20" fill="#fff"/>
        <rect x="4" y="6" width="14" height="10" fill="none" stroke="#000" stroke-width="1.5"/>
        <polyline points="4,6 11,12 18,6" fill="none" stroke="#000" stroke-width="1.5"/>
        <line x1="4" y1="16" x2="9" y2="11" stroke="#000" stroke-width="1.2"/>
        <line x1="18" y1="16" x2="13" y2="11" stroke="#000" stroke-width="1.2"/>
      </svg>
      petra@petrastudioframes.com
    </li>
  </ul>
</section>

<section class="card card--back">
  <div class="brand">
    <span class="brand__name">Petra Voss</span>
    <span class="brand__sub">PHOTOGRAPHY</span>
  </div>
  <p class="tagline">Capturing Life's Moments</p>
</section>

</body>
</html>
```